Business Card Design Project

I need a business card designed from scratch. I have an existing logo that I can upload in Illustrator for modification or redesign.

The Company is called Rank Harbor http://rankharbor.com.au and we provide Search Engine Optimization services to Australian businesses. The current logo signifies an increase in visitors, profits etc...

There are no restrictions as to the redesign - colours, style etc are all open to change.

Cards will be full colour and one sided printed at http://www.printlorvex.com.au so check their requirements for file format and sizes etc.

I will expect all original files upon completion of project.

Target Market(s)

Any business with a web site looking to improve their search engine rankings

Industry/Entity Type

Business

Requirements
Must have
• I like modern, sleek designs. Clean, not fussy, uncluttered.

```html
<!DOCTYPE html>
<html lang="en">
<head>
<meta charset="utf-8">
<title>Rank Harbor – Business Card</title>
<link rel="stylesheet" href="https://fonts.googleapis.com/css2?family=Open+Sans:wght@400;700&display=swap">
<style>
  :root {
    --stage: #3a3a3a;
    --card-light: #eceded;
    --card-dark: #d4d6d8;
    --brand-blue: #1f6fb5;
    --ink: #1d1d1d;
    --rule: #2f6ea8;
    --ghost: rgba(255, 255, 255, 0.55);
    --font-main: "Open Sans", Verdana, sans-serif;
  }
  * { margin: 0; padding: 0; box-sizing: border-box; }
  html, body {
    width: 1200px;
    height: 900px;
    overflow: hidden;
    background: var(--stage);
    font-family: var(--font-main);
  }
  .business-card {
    position: absolute;
    left: 60px;
    top: 151px;
    width: 1080px;
    height: 598px;
    overflow: hidden;
    background: radial-gradient(ellipse at 35% 35%, var(--card-light) 0%, var(--card-dark) 100%);
  }
  .ghost-name {
    position: absolute;
    left: -24px;
    top: 60px;
    font-size: 124px;
    font-weight: 700;
    color: var(--ghost);
    white-space: nowrap;
    line-height: 1;
    letter-spacing: -2px;
  }
  .brand {
    position: absolute;
    left: 250px;
    top: 120px;
    display: flex;
    align-items: center;
    gap: 28px;
  }
  .brand-dot {
    width: 64px;
    height: 64px;
    border-radius: 50%;
    background: var(--brand-blue);
  }
  .brand-name {
    font-size: 92px;
    font-weight: 700;
    color: var(--brand-blue);
    line-height: 1;
    letter-spacing: -1px;
  }
  .person {
    position: absolute;
    left: 136px;
    top: 352px;
    color: var(--ink);
  }
  .person-name {
    font-size: 33px;
    font-weight: 400;
    line-height: 1.2;
  }
  .person-title {
    margin-top: 12px;
    font-size: 23px;
    line-height: 1.2;
  }
  .contact-list {
    position: absolute;
    left: 574px;
    top: 355px;
    list-style: none;
    color: var(--ink);
    font-size: 23px;
    line-height: 32px;
  }
  .contact-item {
    display: flex;
    align-items: center;
    gap: 12px;
  }
  .contact-icon {
    width: 22px;
    height: 22px;
    flex: none;
  }
  .divider {
    position: absolute;
    left: 136px;
    top: 478px;
    width: 806px;
    height: 2px;
    background: var(--rule);
  }
  .tagline {
    position: absolute;
    left: 136px;
    top: 512px;
    width: 820px;
    font-size: 27px;
    font-weight: 700;
    color: var(--brand-blue);
    letter-spacing: 17.5px;
    white-space: nowrap;
  }
</style>
</head>
<body>
  <section class="business-card" aria-label="Rank Harbor business card">
    <div class="ghost-name" aria-hidden="true">Rank Harbor</div>

    <div class="brand">
      <span class="brand-dot" aria-hidden="true"></span>
      <span class="brand-name">Rank Harbor</span>
    </div>

    <div class="person">
      <p class="person-name">Liam Corder</p>
      <p class="person-title">Internet Marketing Consultant</p>
    </div>

    <ul class="contact-list">
      <li class="contact-item">
        <svg class="contact-icon" viewBox="0 0 24 24" aria-hidden="true">
          <path fill="#1d1d1d" d="M3 8c0-2 3-4 9-4s9 2 9 4v2h-5V8.5c-1-.6-2.5-.9-4-.9s-3 .3-4 .9V10H3z"/>
          <path fill="#1d1d1d" d="M7 11h10l3 8H4z"/>
        </svg>
        <span>1300 555 204</span>
      </li>
      <li class="contact-item">
        <svg class="contact-icon" viewBox="0 0 24 24" aria-hidden="true">
          <text x="12" y="19" text-anchor="middle" font-family="Open Sans, sans-serif" font-size="21" font-weight="700" fill="#1d1d1d">@</text>
        </svg>
        <span>liam@rankharbor.com.au</span>
      </li>
      <li class="contact-item">
        <svg class="contact-icon" viewBox="0 0 24 24" aria-hidden="true">
          <circle cx="12" cy="12" r="9" fill="none" stroke="#3a6ea0" stroke-width="2"/>
          <ellipse cx="12" cy="12" rx="4" ry="9" fill="none" stroke="#3a6ea0" stroke-width="1.5"/>
          <line x1="3" y1="12" x2="21" y2="12" stroke="#3a6ea0" stroke-width="1.5"/>
        </svg>
        <span>www.rankharbor.com.au</span>
      </li>
    </ul>

    <div class="divider" aria-hidden="true"></div>

    <p class="tagline">RANKING FOR PROFITS</p>
  </section>
</body>
</html>
```